CD-/Plattencover für Tonträgerfirma
Zielgruppe
Wir sind eine Tonträgerfirma und bewegen uns im Low-Budget-Segment.
Aufgabenstellung
Für eine KLassik Serie benötigen wir 7 Cover, welche aber im Grundlayout immer gleich seinen sollten. Es soll eine erkenntliche Serie entstehen.
Das Thema lautet: Velvet Hour
Die Unterthemen lauten:
1. The Amber Lantern Gathering
2. The Velvet Hour Riverside Suites
3. The Velvet Hour Meadow Steps
4. The Velvet Hour Moonlit Whispers
5. The Copper Table Evenings
6. The Silver Curtain Soirée
7. The Northwind Orchestral Treasures
Wir benötigen nicht das komplette Artwork, sondern ein Frontcover
(12 x 12 cm + 2 cm Beschnitt wg. etwaiger Verschiebung der Positionierung
Fertigstellung (Aufziehen des Inlays und Labels) erfolgt später bei uns im Hause
Wir benötigen später offene psd-Dateien mit allen Ebenen
Wichtig: Schriften nicht gerastert ggfs. Schrift mitliefern

```html
<!DOCTYPE html>
<html lang="en">
<head>
<meta charset="utf-8">
<title>The Silver Curtain Soirée</title>
<link rel="stylesheet" href="https://fonts.googleapis.com/css2?family=Outfit:wght@600&display=swap">
<style>
  :root {
    --gold-light: #d6b640;
    --gold-mid: #c29f2c;
    --gold-deep: #9e7d1a;
    --gold-shadow: #7a5f12;
    --ink-navy: #1b2a34;
    --ring-dark: #6f6a58;
    --ring-grey: #9a9580;
    --ring-pale: #cdbf86;
    --sketch-olive: rgba(34, 32, 8, 0.34);
    --sketch-olive-soft: rgba(34, 32, 8, 0.10);
    --sketch-rust: rgba(95, 28, 8, 0.34);
    --sketch-rust-soft: rgba(95, 28, 8, 0.10);
    --sketch-faint: rgba(70, 55, 10, 0.14);
  }
  html, body {
    margin: 0;
    padding: 0;
    width: 1200px;
    height: 1200px;
    overflow: hidden;
    background: var(--gold-mid);
  }
  .cover {
    position: relative;
    width: 1200px;
    height: 1200px;
    overflow: hidden;
    background:
      repeating-linear-gradient(180deg,
        rgba(255, 238, 160, 0.16) 0 1px,
        rgba(0, 0, 0, 0) 1px 2px,
        rgba(70, 50, 0, 0.14) 2px 3px,
        rgba(0, 0, 0, 0) 3px 5px),
      linear-gradient(100deg, rgba(255,230,140,0.10) 0%, rgba(0,0,0,0) 40%, rgba(60,40,0,0.10) 70%, rgba(0,0,0,0) 100%),
      linear-gradient(165deg, var(--gold-light) 0%, var(--gold-mid) 50%, var(--gold-deep) 100%);
  }
  .cover__art,
  .cover__title {
    position: absolute;
    inset: 0;
    width: 1200px;
    height: 1200px;
  }
  .title-text {
    font-family: "Outfit", "Helvetica Neue", Arial, sans-serif;
    font-weight: 600;
    font-size: 108px;
    letter-spacing: 1px;
    text-anchor: middle;
  }
  .title-ring { fill: none; stroke-linejoin: round; }
  .title-ring--1 { stroke: var(--ring-grey); stroke-width: 40px; opacity: 0.35; }
  .title-ring--2 { stroke: var(--ring-pale); stroke-width: 33px; opacity: 0.55; }
  .title-ring--3 { stroke: var(--ring-dark); stroke-width: 27px; opacity: 0.6; }
  .title-ring--4 { stroke: var(--ring-pale); stroke-width: 21px; opacity: 0.8; }
  .title-ring--5 { stroke: var(--ring-dark); stroke-width: 15px; opacity: 0.8; }
  .title-ring--6 { stroke: var(--ring-pale); stroke-width: 9px; }
  .title-ring--7 { stroke: var(--ring-dark); stroke-width: 4px; }
  .title-fill { fill: var(--ink-navy); }
</style>
</head>
<body>
<main class="cover">
  <svg class="cover__art" viewBox="0 0 1200 1200" xmlns="http://www.w3.org/2000/svg">
    <defs>
      <radialGradient id="tone-right" cx="0.55" cy="0.45" r="0.75">
        <stop offset="0" stop-color="var(--sketch-rust-soft)"/>
        <stop offset="0.8" stop-color="var(--sketch-rust)"/>
        <stop offset="1" stop-color="var(--sketch-rust)"/>
      </radialGradient>
      <radialGradient id="tone-left" cx="0.5" cy="0.6" r="0.75">
        <stop offset="0" stop-color="var(--sketch-olive-soft)"/>
        <stop offset="0.8" stop-color="var(--sketch-olive)"/>
        <stop offset="1" stop-color="var(--sketch-olive)"/>
      </radialGradient>
      <radialGradient id="tone-faint" cx="0.4" cy="0.4" r="0.7">
        <stop offset="0" stop-color="var(--sketch-faint)"/>
        <stop offset="1" stop-color="rgba(70,55,10,0)"/>
      </radialGradient>
    </defs>
    <rect class="sketch sketch--upper-left" role="img"
          aria-label="Faint background sketch lines of a figure, barely visible in the gold"
          x="0" y="0" width="620" height="620" fill="url(#tone-faint)"/>
    <path class="portrait portrait--upper-right" role="img"
          aria-label="Loose ink sketch of a singer's head in profile facing left, drawn in dark rust lines"
          d="M960 0 H1200 V830 C1150 826 1110 812 1080 790 C1040 730 1000 720 980 690 C940 660 900 640 895 600 C905 540 900 470 870 410 C840 330 830 250 840 170 C860 90 900 30 960 0 Z"
          fill="url(#tone-right)"/>
    <path class="portrait portrait--lower-left" role="img"
          aria-label="Loose ink sketch of a singer with head tilted back, mouth open, drawn in dark olive lines"
          d="M0 830 C60 740 170 690 300 685 C420 680 520 730 590 800 C660 860 720 940 730 1000 C740 1060 760 1130 770 1200 H0 Z"
          fill="url(#tone-left)"/>
  </svg>

  <svg class="cover__title" viewBox="0 0 1200 1200" xmlns="http://www.w3.org/2000/svg">
    <title>The Silver Curtain Soirée</title>
    <defs>
      <g id="title-lines" class="title-text">
        <text x="612" y="432">THE SILVER</text>
        <text x="612" y="584">CURTAIN</text>
        <text x="612" y="736">SOIRÉE</text>
      </g>
    </defs>
    <use href="#title-lines" class="title-ring title-ring--1"/>
    <use href="#title-lines" class="title-ring title-ring--2"/>
    <use href="#title-lines" class="title-ring title-ring--3"/>
    <use href="#title-lines" class="title-ring title-ring--4"/>
    <use href="#title-lines" class="title-ring title-ring--5"/>
    <use href="#title-lines" class="title-ring title-ring--6"/>
    <use href="#title-lines" class="title-ring title-ring--7"/>
    <g class="title-text title-fill">
      <text x="612" y="432">THE SILVER</text>
      <text x="612" y="584">CURTAIN</text>
      <text x="612" y="736">SOIRÉE</text>
    </g>
  </svg>
</main>
</body>
</html>
```